GLP letterhead

We need a letterhead design for our new company based in Los Angeles called "Gold Lantern Pictures". We develop film and television projects. We work with investors, financiers, film production companies, film distribution and sales companies as well as studios. We would like to incorporate our logo (see attached) but make the letterhead simple and elegant. We need to include: logo, company address, phone number and company website.
Updates

Hello designers, Thanks for your submissions. For our letterhead, we are looking for something more simple and elegant. No heavy bars or lines. Make it feel light and clean. Not a lot of ink on the page. Use the logo and contact info but think "clean", "streamlined" and mostly white paper. Looking forward to seeing more... thanks! Gold Lantern Pictures team

Target Market(s)

Studio executives, talent agents and agencies, financiers, investors.

Industry/Entity Type

It Company

Requirements
Must have
• Gold Lantern Pictures logo (see attached). Logo may be cropped and altered appropriately for elegant letterhead design.
• Please include:
• COMPANY ADDRESS:
• Ridgeway Studio Park
• 2850 Halverson Street
• Tower Annex, 4th Floor
• Manhattan Beach, CA 90412
• COMPANY WEBSITE:
• www.goldlanternpicturesco.example
• COMPANY PHONE NUMBER:
• 310-555-0148

```html
<!DOCTYPE html>
<html lang="en">
<head>
<meta charset="utf-8">
<title>Gold Lantern Pictures — Letterhead</title>
<link rel="stylesheet" href="https://fonts.googleapis.com/css2?family=Open+Sans:wght@400;600&display=swap">
<style>
  :root {
    --backdrop: #e4e4e2;
    --paper: #ffffff;
    --mark-dark: #0f1a1f;
    --brand-blue: #2a8fc9;
    --tagline: #9fb3bf;
    --rule: #cfd8de;
    --ink: #3a3a3a;
    --ghost: #f4f5f5;
  }
  * { margin: 0; padding: 0; box-sizing: border-box; }
  html, body {
    width: 950px; height: 1200px; overflow: hidden;
    background: var(--backdrop);
    font-family: "Open Sans", Arial, sans-serif;
  }
  .sheet {
    position: absolute; left: 52px; top: 50px;
    width: 846px; height: 1098px;
    background: var(--paper);
  }
  .brand {
    position: absolute; top: 22px; left: 0; width: 100%;
    display: flex; flex-direction: column; align-items: center;
  }
  .brand-disc {
    width: 112px; height: 112px; border-radius: 50%;
    background: var(--mark-dark);
  }
  .brand-name {
    margin-top: 12px;
    font-weight: 600; font-size: 17px; line-height: 20px;
    letter-spacing: 2px; color: var(--brand-blue);
    text-align: center; text-transform: uppercase;
  }
  .brand-tagline {
    margin-top: 4px;
    font-size: 6px; letter-spacing: 2.6px;
    color: var(--tagline); text-transform: uppercase;
  }
  .ghost-disc {
    position: absolute; left: 224px; top: 304px;
    width: 392px; height: 392px; border-radius: 50%;
    background: var(--ghost);
  }
  .footer {
    position: absolute; left: 0; bottom: 0; width: 100%; height: 64px;
    border-top: 2px solid var(--rule);
    padding: 12px 14px 0 14px;
    display: flex; justify-content: space-between;
    font-size: 13px; line-height: 18px; color: var(--ink);
  }
  .contact { text-align: right; }
  .contact-line { display: flex; align-items: center; justify-content: flex-end; gap: 6px; }
  .contact-line svg { width: 10px; height: 10px; }
</style>
</head>
<body>
  <main class="sheet">
    <header class="brand">
      <div class="brand-disc"></div>
      <div class="brand-name">Gold Lantern<br>Pictures</div>
      <div class="brand-tagline">A Media Entertainment Company</div>
    </header>

    <div class="ghost-disc"></div>

    <footer class="footer">
      <address class="address" style="font-style:normal">
        Ridgeway Studio Park 2850 Halverson Street Tower Annex,<br>
        4th Floor Manhattan Beach, CA 90412
      </address>
      <div class="contact">
        <div class="contact-line">
          <svg viewBox="0 0 10 10" aria-hidden="true"><path d="M2 1 L4 3 L3 4 Q4 6 6 7 L7 6 L9 8 L8 9 Q3 9 1 2 Z" fill="none" stroke="#555" stroke-width="0.9"/></svg>
          <span>310-555-0148</span>
        </div>
        <div class="contact-line">
          <svg viewBox="0 0 10 10" aria-hidden="true"><circle cx="5" cy="5" r="4" fill="none" stroke="#555" stroke-width="0.9"/><ellipse cx="5" cy="5" rx="1.8" ry="4" fill="none" stroke="#555" stroke-width="0.7"/><line x1="1" y1="5" x2="9" y2="5" stroke="#555" stroke-width="0.7"/></svg>
          <span>www.goldlanternpicturesco.example</span>
        </div>
      </div>
    </footer>
  </main>
</body>
</html>
```